TOASTED COCONUT CHIPS

My company is a food company specialised in coconut products. The subject project is to design the package bag and respective simple shipping case for toasted coconut chips for two flavors: one is original and the other is cinnamon. I also need a logo design for the brand "pelvo".

I would like the bag looks simple, classy and attractive. Or the other way that it could look cute and fun.

The design will include two flavors: original/sea salt and cinnamon
The design need to be fit in 40g pouch bag and 20g bag.
Need the design of the bag and subsequently the shipping case.
Updates

Project Deadline Extended Reason: As per request of some designers, the deadline will be extended by 5 days. Added Tuesday, November 8, 2016

Target Market(s)

age 8 to 40
sell in cafeteria and vending machine

Industry/Entity Type

It Company

Logo Text

simple and direct

Requirements
Must have
• golden coconut chips picture on the front side.
• the bag should looks clean but attractive.
• Otherwise, it has to be very colourful to attract eye balls.
• I need the design can be fit in a 40g pouch and 20g cutie size bag
Should not have
• Should not look Asian food.

```html
<!DOCTYPE html>
<html lang="en">
<head>
<meta charset="utf-8">
<title>pelvo Toasted Coconut Chips – Cinnamon</title>
<link rel="stylesheet" href="https://fonts.googleapis.com/css2?family=Alfa+Slab+One&family=Cinzel:wght@400;700&family=Great+Vibes&family=Arimo:wght@400;700&family=Tinos&display=swap">
<style>
  :root {
    --backdrop: #fde3c2;
    --bag-cream: #f5ede0;
    --bag-shade: #ebe0cf;
    --brown-dark: #4a2c16;
    --brown-mid: #7a4a24;
    --brown-gold: #a8743f;
    --beige-light: #e4cfae;
    --chip-orange: #e98a4d;
    --chip-light: #f6b07a;
    --text-grey: #6e665e;
    --white: #ffffff;
  }
  * { margin: 0; padding: 0; box-sizing: border-box; }
  html, body {
    width: 964px;
    height: 1200px;
    overflow: hidden;
    background: var(--backdrop);
  }
  .canvas {
    position: relative;
    width: 964px;
    height: 1200px;
  }
  .bag {
    position: absolute;
    left: 169px;
    top: 167px;
    width: 632px;
    height: 860px;
    background: linear-gradient(180deg, var(--bag-cream) 0%, #f8f2e8 45%, var(--bag-shade) 100%);
    overflow: hidden;
  }
  .top-seal {
    position: absolute;
    left: 0; top: 0;
    width: 100%;
    height: 14px;
    background: linear-gradient(90deg, var(--brown-mid), var(--brown-dark) 50%, var(--brown-mid));
  }
  .bottom-seal {
    position: absolute;
    left: 0; bottom: 0;
    width: 100%;
    height: 34px;
    border-top: 1px solid #ded2bf;
    background: repeating-linear-gradient(180deg, var(--bag-shade) 0 3px, #e3d7c4 3px 4px);
  }
  .brand {
    position: absolute;
    top: 120px;
    left: 0;
    width: 100%;
    display: flex;
    justify-content: center;
    align-items: center;
    gap: 12px;
  }
  .brand-dot {
    width: 22px;
    height: 22px;
    border-radius: 50%;
    background: var(--brown-dark);
  }
  .brand-name {
    font-family: "Arimo", sans-serif;
    font-weight: 700;
    font-size: 46px;
    color: var(--brown-dark);
    letter-spacing: 1px;
  }
  .title {
    position: absolute;
    left: 0;
    width: 100%;
    text-align: center;
    background: linear-gradient(90deg, var(--beige-light) 0%, #c9a57a 45%, var(--brown-gold) 100%);
    -webkit-background-clip: text;
    background-clip: text;
    color: transparent;
  }
  .title-toasted {
    top: 218px;
    font-family: "Alfa Slab One", serif;
    font-size: 74px;
    font-weight: 400;
    line-height: 1;
  }
  .title-coconut {
    top: 292px;
    font-family: "Alfa Slab One", serif;
    font-size: 82px;
    line-height: 1;
  }
  .title-chips {
    top: 372px;
    font-family: "Cinzel", serif;
    font-weight: 700;
    font-size: 42px;
    line-height: 1;
  }
  .flavour {
    position: absolute;
    top: 436px;
    left: 0;
    width: 100%;
    text-align: center;
    font-family: "Cinzel", serif;
    font-size: 40px;
    line-height: 1;
    color: var(--brown-dark);
    letter-spacing: 1px;
  }
  .claim {
    position: absolute;
    top: 488px;
    left: 178px;
    width: 273px;
    text-align: center;
    font-family: "Great Vibes", cursive;
    font-size: 33px;
    line-height: 1;
    white-space: nowrap;
    color: var(--brown-gold);
  }
  .free-from {
    position: absolute;
    top: 554px;
    left: 92px;
    width: 320px;
    text-align: center;
    font-family: "Arimo", sans-serif;
    font-size: 17px;
    line-height: 20px;
    color: var(--text-grey);
  }
  .chips-photo {
    position: absolute;
    left: 380px;
    top: 440px;
    width: 252px;
    height: 320px;
    clip-path: polygon(120px 0, 252px 0, 252px 320px, 160px 320px, 60px 260px, 30px 200px, 30px 120px, 80px 100px, 100px 40px);
    background: radial-gradient(circle at 55% 45%, var(--chip-light) 0%, var(--chip-orange) 60%, #d9723a 100%);
  }
  .diet-band {
    position: absolute;
    left: 0;
    top: 709px;
    width: 531px;
    height: 31px;
    border-radius: 0 16px 16px 0;
    background: var(--brown-mid);
    display: flex;
    align-items: center;
    padding-left: 75px;
    font-family: "Tinos", serif;
    font-size: 19px;
    white-space: nowrap;
    color: var(--white);
    letter-spacing: 0.5px;
  }
  .net-weight {
    position: absolute;
    top: 752px;
    left: 0;
    width: 100%;
    text-align: center;
    font-family: "Tinos", serif;
    font-size: 22px;
    color: var(--brown-dark);
  }
</style>
</head>
<body>
<div class="canvas">
  <div class="bag">
    <div class="top-seal"></div>

    <div class="brand">
      <span class="brand-dot"></span>
      <span class="brand-name">pelvo</span>
    </div>

    <h1 class="title title-toasted">Toasted</h1>
    <div class="title title-coconut">COCONUT</div>
    <div class="title title-chips">CHIPS</div>

    <div class="flavour">CINNAMON</div>

    <div class="chips-photo" role="img" aria-label="Pile of golden cinnamon toasted coconut chips"></div>

    <div class="claim">Good Source of Fiber</div>

    <p class="free-from">
      no cholesterol no preservative<br>
      no artifical color<br>
      no artificial flavouring
    </p>

    <div class="diet-band">GLUTEN FREE VEGAN DAIRY FREE</div>

    <div class="net-weight">Net weight: 20 g (0.7 oz)</div>

    <div class="bottom-seal"></div>
  </div>
</div>
</body>
</html>
```